Economics of an Assumption vs Obtaining a New Loan at Current Market Rate

I need to marketing flyer that has fields that calculate mortgage payments amongst other calculations. I have a rough draft that I will attach.

The idea is to provide a tool for a real estate agent to use to illustrate to a potential buyer what a payment would be if they assumed the existing loan on the house or took out a new loan at current market.

The flyer needs to be able to allow an agent to drop in their logo, photo, and contact along with the loan officers photo and contact info.

You can google open house flyer to see examples of what the overall artwork and presentation can look like.

Target Market(s)

Home Buyers

Industry/Entity Type

Real Estate

Colors
F0912C
F2A743
F7CA91
FBE8D2
FDF5EE
EE7325
F08F49
F5BC92
FAE3D3
FDF4ED

Requirements
Must have
• A way to calculate mortgage payment
Nice to have
• Photo and logo drop ins

```html
<!DOCTYPE html>
<html lang="en">
<head>
<meta charset="utf-8">
<title>Keyhaven – Rate-Ready Flyer</title>
<link rel="stylesheet" href="https://fonts.googleapis.com/css2?family=Bebas+Neue&family=Kumbh+Sans:wght@400;500;600;700;800&display=swap">
<style>
  :root {
    --backdrop: #6e6e6e;
    --paper: #ffffff;
    --orange: #ee7325;
    --orange-soft: #f08f49;
    --ink: #1f1f1f;
    --field-line: #9a9a9a;
    --sky-top: #7c9fd4;
    --sky-mid: #a8a3c9;
    --stucco: #b78a5a;
    --gravel: #a99c93;
  }
  * { box-sizing: border-box; margin: 0; padding: 0; }
  html, body { width: 1200px; height: 904px; overflow: hidden; }
  body {
    background: var(--backdrop);
    font-family: "Kumbh Sans", sans-serif;
    color: var(--ink);
  }
  .flyer {
    position: absolute;
    left: 251px; top: 0;
    width: 698px; height: 904px;
    background: var(--paper);
    overflow: hidden;
  }
  .hero-photo {
    position: absolute; left: 0; top: 0;
    width: 698px; height: 395px;
    background: linear-gradient(180deg,
      var(--sky-top) 0%, var(--sky-mid) 40%,
      #c79d6e 55%, var(--stucco) 78%,
      var(--gravel) 88%, #8f837c 100%);
  }
  .brand-badge { position: absolute; left: 0; top: 0; }
  .brand-name {
    position: absolute; left: 48px; top: 68px;
    font-size: 46px; font-weight: 600;
    color: var(--orange); letter-spacing: -0.5px;
  }
  .price-bar {
    position: absolute; left: 41px; top: 408px;
    width: 294px; height: 26px;
    border: 1px solid #c9c9c9; border-radius: 5px;
    overflow: hidden;
  }
  .price-bar .price-label {
    display: block; width: 143px; height: 100%;
    background: var(--orange); color: #fff;
    font-weight: 800; font-size: 14px;
    line-height: 26px; padding-left: 6px;
  }
  .section-title {
    position: absolute; left: 41px; top: 449px;
    font-size: 15px; font-weight: 800;
  }
  .new-title {
    position: absolute; left: 362px; top: 437px;
    font-family: "Bebas Neue", sans-serif; font-weight: 400;
    font-size: 28px; letter-spacing: -0.8px; line-height: 30px;
    white-space: nowrap;
  }
  .label {
    position: absolute; font-size: 13px; font-weight: 700;
    transform: translateY(-50%); white-space: nowrap;
  }
  .field {
    position: absolute; height: 22px;
    border: 1px solid var(--field-line);
    transform: translateY(-50%);
    font-size: 8.5px; font-weight: 500;
    display: flex; align-items: center; justify-content: center;
    white-space: nowrap;
  }
  .field.hint-lg { font-size: 11px; }
  .field.wide { left: 171px; width: 165px; }
  .field.wide-r { left: 492px; width: 165px; }
  .certified-line {
    position: absolute; left: 40px; top: 700px; width: 620px;
    font-size: 24.5px; font-weight: 800; color: var(--orange);
    letter-spacing: -0.6px; white-space: nowrap; line-height: 30px;
  }
  .dropin {
    position: absolute; top: 746px;
    width: 142px; height: 129px;
    border: 1px solid var(--field-line);
  }
</style>
</head>
<body>
<main class="flyer">
  <div class="hero-photo" role="img" aria-label="Photo of a tan stucco single-storey home with tile roof and desert landscaping under a cloudy dusk sky"></div>

  <svg class="brand-badge" width="340" height="180" viewBox="0 0 340 180" aria-hidden="true">
    <ellipse cx="152" cy="38" rx="181" ry="138" fill="var(--orange)"/>
    <ellipse cx="145" cy="33" rx="178" ry="135" fill="var(--paper)"/>
  </svg>
  <div class="brand-name">Keyhaven</div>

  <div class="price-bar"><span class="price-label">PURCHASE PRICE:</span></div>

  <h2 class="section-title">CURRENT MORTGAGE:</h2>
  <span class="label" style="left:41px;top:481px">Lone amount:</span>
  <div class="field wide" style="top:481px"></div>
  <span class="label" style="left:41px;top:509px">Interest rate:</span>
  <div class="field wide" style="top:509px"></div>
  <span class="label" style="left:41px;top:535px">Principal interest:</span>
  <div class="field wide" style="top:535px"></div>
  <span class="label" style="left:41px;top:563px">Mortgage insurance:</span>
  <div class="field wide" style="top:563px"></div>
  <span class="label" style="left:41px;top:590px">TOTAL:</span>
  <div class="field wide" style="top:590px">Principal interest + Mortgage insurance</div>

  <span class="label" style="left:40px;top:618px">Years</span>
  <div class="field" style="left:80px;width:46px;top:618px"></div>
  <span class="label" style="left:140px;top:618px">Months</span>
  <div class="field" style="left:193px;width:46px;top:618px"></div>
  <span class="label" style="left:253px;top:618px">left on loan</span>

  <span class="label" style="left:40px;top:646px">Telta</span>
  <div class="field" style="left:80px;width:165px;top:646px;font-size:9.5px">Purchase Price minus loan amount</div>

  <span class="label" style="left:39px;top:673px">Payment difference</span>
  <div class="field wide" style="top:673px;font-size:10px">difference between totals</div>

  <h2 class="new-title">NEW MORTGAGE 10% DOWN PAYMENT</h2>
  <span class="label" style="left:362px;top:481px">Lone amount:</span>
  <div class="field wide-r hint-lg" style="top:481px">90% of purchase price</div>
  <span class="label" style="left:362px;top:509px">Market rate:</span>
  <div class="field wide-r" style="top:509px"></div>
  <span class="label" style="left:362px;top:535px">Principal interest:</span>
  <div class="field wide-r" style="top:535px"></div>
  <span class="label" style="left:362px;top:563px">Mortgage insurance:</span>
  <div class="field wide-r" style="top:563px"></div>
  <span class="label" style="left:362px;top:590px">TOTAL:</span>
  <div class="field wide-r" style="top:590px">Principal interest + Mortgage insurance</div>

  <span class="label" style="left:362px;top:618px">Term</span>
  <div class="field" style="left:402px;width:46px;top:618px"></div>
  <span class="label" style="left:462px;top:618px">Years</span>
  <div class="field" style="left:515px;width:46px;top:618px"></div>

  <span class="label" style="left:362px;top:646px">Down payment amount</span>
  <div class="field" style="left:515px;width:142px;top:646px"></div>

  <p class="certified-line">THIS PROPERTY IS “RATE-READY CERTIFIED”</p>

  <div class="dropin" style="left:42px"></div>
  <div class="dropin" style="left:199px"></div>
  <div class="dropin" style="left:356px"></div>
  <div class="dropin" style="left:514px"></div>
</main>
</body>
</html>
```